Postcard Design

Velvet Petal a Waxing Boutique - We need a postcard Front of it with a boarder done as a dainty picture frame and inside listing our services menu. We would like the picture frame to be white and the background to be a light grey and service menu writing in white as well. On back we need name, address, etc. We weould like the name to be in Turquise. Do you help design logos?
menu sheet -
Facial Services:
Brow Shaping $18
Lip - $12
Brow and Lip Combo $25
Sideburns - $12
Nose $10
Ears $10
Full Face Combo Excluding Brows $40
Full Face Combo w/ Brow Shaping $55
Lash Tint $20
Brow Tint $15
(This is to darken brows only)
Brow Shaping + Brow Tint $33

BODY WAXING :
Neck $15
Shoulders$20
Full back $45
Chest $45
(Abdomen Included)
Abdomen $15
Underarms $15
Full Arm $40
Half Arm $30
Full Leg $60
(Bikini line not included, This covers the upper thigh down to the feet and toes)
Half Leg $45
(Upper or Lower leg)
Modest Bikini - $35 Female Only
Brazilian Bikini $55 Female Only
Buttocks $20

Whats So Special About Our Pricing? Its Simple:
*Straight Forward Prices and No Tipping Policy!

Back of Card -

Velvet Petal
{Waxing Boutique}

Located in Studios Marigo
415 W. Corbin Dale Blvd
Suite 17
Rockwall, TX 75849
(972)514-2078

```html
<!DOCTYPE html>
<html lang="en">
<head>
<meta charset="utf-8">
<title>Velvet Petal – Postcard</title>
<link rel="stylesheet" href="https://fonts.googleapis.com/css2?family=Raleway:wght@600;700;800&family=Kalam:wght@700&display=swap">
<style>
  :root {
    --page: #000000;
    --card: #d5d5d7;
    --white: #ffffff;
    --accent: #e8401c;
    --turquoise: #17a3a3;
    --menu-shadow: rgba(0, 0, 0, .55);
    --panel: #333333;
    --rule: #1a1a1a;
  }
  * { margin: 0; padding: 0; box-sizing: border-box; }
  html, body { width: 785px; height: 1200px; overflow: hidden; background: var(--page); }
  body { position: relative; font-family: "Raleway", Arial, sans-serif; }

  .card { position: absolute; left: 37px; width: 711px; background: var(--card); overflow: hidden; }
  .card--front { top: 37px; height: 546px; }
  .card--back { top: 616px; height: 555px; }

  .frame { position: absolute; inset: 14px; border: 3px solid var(--white); }
  .frame::after { content: ""; position: absolute; inset: 6px; border: 1px solid var(--white); }

  .brand-tab { position: absolute; top: 0; width: 167px; height: 120px; }
  .brand-tab svg { position: absolute; inset: 0; }
  .brand-tab .brand-name {
    position: absolute; left: 0; right: 0; top: 58px; text-align: center;
    font-weight: 800; font-size: 19px; color: var(--turquoise); letter-spacing: .5px;
  }
  .brand-tab .brand-dot {
    position: absolute; left: 50%; top: 24px; width: 22px; height: 22px; margin-left: -11px;
    border-radius: 50%; background: var(--turquoise);
  }
  .card--front .brand-tab { left: 280px; }
  .card--back .brand-tab { left: 106px; height: 137px; width: 160px; }
  .card--back .brand-tab .brand-name { top: 66px; }
  .card--back .brand-tab .brand-dot { top: 30px; }

  .photo { position: absolute; border-radius: 50%; border: 3px solid var(--white); }
  .photo--wax { left: 100px; top: 40px; width: 120px; height: 120px; background: radial-gradient(circle at 40% 40%, #f3d2c4, #d9a58f); }
  .photo--lash { left: 191px; top: 80px; width: 88px; height: 88px; background: radial-gradient(circle at 50% 50%, #d8b15a, #8c6a3a); }
  .photo--eye { left: 450px; top: 78px; width: 88px; height: 88px; background: radial-gradient(circle at 50% 45%, #e9c8b4, #b88a74); }
  .photo--spa { left: 540px; top: 43px; width: 120px; height: 120px; background: radial-gradient(circle at 55% 45%, #f0cfc0, #d79c8a); }

  .menu { position: absolute; left: 0; right: 0; text-align: center; color: var(--white); }
  .menu h2 { font-weight: 800; font-size: 20px; color: var(--accent); text-decoration: underline; text-underline-offset: 3px; margin-bottom: 2px; }
  .menu p { font-weight: 700; font-size: 14.5px; line-height: 24px; text-transform: uppercase; text-shadow: 0 1px 2px var(--menu-shadow); }
  .menu .note { color: var(--accent); text-shadow: none; }
  .menu--body { top: 160px; padding: 0 58px; }
  .menu--facial { top: 310px; padding: 0 58px; }

  .ribbon { position: absolute; left: 76px; top: 463px; width: 551px; height: 35px; }
  .ribbon svg { position: absolute; inset: 0; }
  .ribbon span {
    position: absolute; inset: 0; display: flex; align-items: center; justify-content: center;
    font-family: "Kalam", cursive; font-size: 16px; color: var(--white); text-transform: uppercase; letter-spacing: .5px;
  }

  .boutique { position: absolute; left: 59px; top: 148px; width: 240px; text-align: center; color: var(--turquoise); font-family: "Kalam", cursive; }
  .boutique__name { font-size: 25px; line-height: 28px; text-transform: uppercase; letter-spacing: 1px; }
  .boutique__tag { font-size: 14px; text-transform: uppercase; letter-spacing: 1px; }

  .thumb { position: absolute; border-radius: 50%; border: 3px solid var(--white); }
  .thumb--palette { left: 24px; top: 224px; width: 86px; height: 86px; background: linear-gradient(135deg, #3a3a3a, #c95f8a 55%, #5a3a2a); }
  .thumb--model { left: 249px; top: 222px; width: 90px; height: 90px; background: radial-gradient(circle at 50% 45%, #f3d4bd, #d9a07f); }

  .offer { position: absolute; left: 130px; top: 211px; width: 110px; height: 115px; }
  .offer svg { position: absolute; inset: 0; }
  .offer span {
    position: absolute; left: 0; right: 0; top: 30px; text-align: center; color: var(--white);
    font-weight: 800; font-size: 19px; line-height: 24px;
  }

  .phone { position: absolute; left: 68px; top: 336px; display: flex; align-items: center; gap: 10px; color: var(--accent); font-weight: 700; font-size: 25px; }

  .address { position: absolute; left: 19px; top: 396px; width: 327px; height: 140px; background: var(--panel); color: var(--white); text-align: center; font-weight: 800; font-size: 18px; line-height: 29px; padding-top: 10px; }
  .address b { color: var(--accent); }

  .stamp { position: absolute; left: 536px; top: 19px; width: 160px; height: 160px; background: #000; border: 2px solid #fff; }
  .mail-lines { position: absolute; left: 387px; top: 244px; width: 293px; }
  .mail-lines i { display: block; height: 2px; background: var(--rule); margin-bottom: 41px; }
</style>
</head>
<body>

<section class="card card--front">
  <div class="frame"></div>

  <div class="photo photo--wax" role="img" aria-label="Photo of wax being applied with a spatula"></div>
  <div class="photo photo--lash" role="img" aria-label="Close-up photo of lash tinting"></div>
  <div class="photo photo--eye" role="img" aria-label="Close-up photo of a shaped brow"></div>
  <div class="photo photo--spa" role="img" aria-label="Photo of smooth skin with a flower"></div>

  <div class="brand-tab">
    <svg width="167" height="120" viewBox="0 0 167 120"><polygon points="0,0 167,0 167,98 83.5,120 0,98" fill="#fff"/></svg>
    <div class="brand-dot"></div>
    <div class="brand-name">VELVET PETAL</div>
  </div>

  <div class="menu menu--body">
    <h2>BODY WAXING :</h2>
    <p>Neck $15, Shoulders$20, Full Back $45, Chest $45(Abdomen Included)
    Abdomen $15, Underarms $15, Full Arm $40, Half Arm $30, Full Leg $60
    <span class="note">(Bikini line not included, this covers the upper thigh down to the feet and toes)</span>Half Leg $45,<span class="note">(Upper or Lower Leg)</span>, Modest Bikini - $35 Female Only Brazilian Bikini $55 Female Only, Buttocks $20</p>
  </div>

  <div class="menu menu--facial">
    <h2>FACIAL SERVICES:</h2>
    <p>Brow Shaping $18, Lip - $12, Brow and Lip Combo $25<br>
    Sideburns - $12, Nose $10, Ears $10, Full Face Combo Excluding Brows $40<br>
    Full Face Combo w/ Brow Shaping $55, Lash Tint $20, Brow Tint $15<br>
    <span class="note">(This is to darken brows only)</span>, Brow Shaping + Brow Tint $33</p>
  </div>

  <div class="ribbon">
    <svg width="551" height="35" viewBox="0 0 551 35"><polygon points="0,2 551,2 536,17.5 551,33 0,33 15,17.5" fill="#e8401c"/></svg>
    <span>Straight forward prices and no tipping policy!</span>
  </div>
</section>

<section class="card card--back">
  <div class="brand-tab">
    <svg width="160" height="137" viewBox="0 0 160 137"><polygon points="0,0 160,0 160,115 80,137 0,115" fill="#fff"/></svg>
    <div class="brand-dot"></div>
    <div class="brand-name">VELVET PETAL</div>
  </div>

  <div class="boutique">
    <div class="boutique__name">Velvet Petal</div>
    <div class="boutique__tag">{Waxing Boutique}</div>
  </div>

  <div class="thumb thumb--palette" role="img" aria-label="Photo of a makeup palette"></div>
  <div class="offer">
    <svg width="110" height="115" viewBox="0 0 110 115">
      <circle cx="55" cy="54" r="52" fill="#e8401c" stroke="#fff" stroke-width="3"/>
      <polygon points="72,96 92,114 86,88" fill="#e8401c"/>
    </svg>
    <span>SPECIAL<br>OFFER</span>
  </div>
  <div class="thumb thumb--model" role="img" aria-label="Photo of a smiling client"></div>

  <div class="phone">
    <svg width="34" height="34" viewBox="0 0 24 24" aria-hidden="true"><path fill="#e8401c" d="M6.6 10.8a15.1 15.1 0 0 0 6.6 6.6l2.2-2.2a1 1 0 0 1 1-.25 11.4 11.4 0 0 0 3.6.57 1 1 0 0 1 1 1V20a1 1 0 0 1-1 1A17 17 0 0 1 3 4a1 1 0 0 1 1-1h3.5a1 1 0 0 1 1 1c0 1.25.2 2.45.57 3.57a1 1 0 0 1-.25 1z"/><path fill="none" stroke="#e8401c" stroke-width="1.6" stroke-linecap="round" d="M14 3a7 7 0 0 1 7 7M14 6.5A3.5 3.5 0 0 1 17.5 10"/></svg>
    <span>(972)514-2078</span>
  </div>

  <div class="address">
    <b>ADDRESS:</b> STUDIOS MARIGO<br>
    415 W. CORBIN DALE BLVD<br>
    SUITE 17<br>
    ROCKWALL, TX 75849
  </div>

  <div class="stamp"></div>
  <div class="mail-lines"><i></i><i></i><i></i><i></i><i></i></div>
</section>

</body>
</html>
```